IT Tradingsystem for car dealers needs Business Card Design

We need a fresh and modern design for our new business cards.

We develop a it-business system for car dealers in Sweden, Norway and on our way down to further countries in Europe, hence the namechange to BrolaTek Europe AB. The site can be found at www.brolatek-example.com. The startpage is also in for an update/modernization soon so don't take to much from here.

We are looking to print double sided, 4-colour cards.

We want to look professional, modern and serious. Open to cooler suggestions, but not too crazy. We need to make a good and serious impression on our potential customers. It needs to reflect our scandinavian design values and layout.

Preferably with the full BrolaTek logo in good size on the back, so the small print on the logo can be read easily.

Text that needs to go on the cards:
-------

Per Oskar Fjellström
Founder

Direct +46 70-512 96 47
Support 08-612 57 394
po.fjellstrom@brolatek-example.com

BrolaTek Europe AB
Box 8617
104 29 Stockholm

Brolatek-example.com
Saljportalen-example.se

--------
Good luck and thanks!

PS. If you need more input or see what our previous cards looked like, don't hesitate to contact me!

Target Market(s)

Decision makers / executives at brand cardealers

Industry/Entity Type

Automotive

Contact Information for Business Card

Normal size

Requirements
Must have
• Full logo
Nice to have
• Base on our orange colors
Should not have
• No fonts with serif, and not too much graphics

```html
<!DOCTYPE html>
<html lang="sv">
<head>
<meta charset="utf-8">
<title>BrolaTek – business cards</title>
<link href="https://fonts.googleapis.com/css2?family=Noto+Sans:wght@400;700&display=swap" rel="stylesheet">
<style>
  :root {
    --orange-light: #f2a05c;
    --orange-deep: #ee7410;
    --ink: #1b1b1b;
    --paper: #ffffff;
    --backdrop: #ecebe8;
  }
  * { margin: 0; padding: 0; box-sizing: border-box; }
  html, body {
    width: 1200px; height: 872px; overflow: hidden;
    background: var(--backdrop);
    font-family: "Noto Sans", Arial, sans-serif;
    color: var(--ink);
  }
  .card {
    position: absolute;
    width: 560px; height: 320px;
    background: var(--paper);
    box-shadow: 0 6px 18px rgba(0,0,0,.18);
    overflow: hidden;
  }
  .card-front { left: 40px; top: 130px; }
  .card-back  { left: 600px; top: 420px; }
  .card-shapes { position: absolute; inset: 0; }

  .brand { position: absolute; display: flex; align-items: center; }
  .brand-square { background: var(--orange-deep); flex: none; }
  .brand-name { font-weight: 700; color: var(--ink); line-height: 1; }
  .brand-tagline { position: absolute; color: var(--ink); white-space: nowrap; }

  .card-front .brand { left: 28px; top: 82px; gap: 10px; }
  .card-front .brand-square { width: 22px; height: 22px; }
  .card-front .brand-name { font-size: 30px; }
  .card-front .brand-tagline { left: 60px; top: 116px; font-size: 8.5px; }

  .holder { position: absolute; right: 30px; top: 26px; text-align: right; }
  .holder-name { font-size: 23px; font-weight: 700; white-space: nowrap; }
  .holder-role { font-size: 19px; color: var(--paper); letter-spacing: 5px; margin-top: -4px; }

  .contact {
    position: absolute; left: 332px; top: 122px;
    font-size: 11px; font-weight: 700; line-height: 1.35;
    white-space: nowrap;
  }
  .contact p + p { margin-top: 12px; }

  .address {
    position: absolute; left: 70px; top: 222px;
    font-size: 15px; font-weight: 700; line-height: 1.3;
  }

  .card-back .brand { left: 64px; top: 92px; gap: 22px; }
  .card-back .brand-square { width: 64px; height: 64px; }
  .card-back .brand-name { font-size: 72px; letter-spacing: -1px; }
  .card-back .brand-tagline { left: 150px; top: 178px; font-size: 15px; letter-spacing: .3px; }
  .back-links {
    position: absolute; left: 0; right: 0; top: 244px;
    text-align: center; font-size: 17px; line-height: 1.2;
  }
</style>
</head>
<body>

<section class="card card-front" aria-label="Business card, front">
  <svg class="card-shapes" width="560" height="320" viewBox="0 0 560 320" aria-hidden="true">
    <path d="M262,0 L560,0 L560,320 L0,320 L0,262 L120,160 C200,92 240,60 262,0 Z" fill="var(--orange-light)"/>
    <path d="M316,118 L338,98 L548,98 L548,232 Q460,272 330,262 Z" fill="var(--orange-deep)"/>
    <polygon points="478,320 560,256 560,320" fill="var(--orange-deep)"/>
    <line x1="458" y1="322" x2="562" y2="240" stroke="var(--paper)" stroke-width="4"/>
  </svg>

  <div class="brand">
    <span class="brand-square"></span>
    <span class="brand-name">BrolaTek</span>
  </div>
  <div class="brand-tagline">ValuTest | Remarketing | saljportalen-example.se</div>

  <div class="holder">
    <div class="holder-name">Per Oskar Fjellström</div>
    <div class="holder-role">founder</div>
  </div>

  <div class="contact">
    <p>Direct +46 70-512 96 47<br>Support 08-612 57 394</p>
    <p>po.fjellstrom@brolatek-example.com</p>
    <p>www.brolatek-example.com<br>www.saljportalen-example.se</p>
  </div>

  <div class="address">
    BrolaTek Europe AB<br>
    Box 8617<br>
    104 29 Stockholm
  </div>
</section>

<section class="card card-back" aria-label="Business card, back">
  <div class="brand">
    <span class="brand-square"></span>
    <span class="brand-name">BrolaTek</span>
  </div>
  <div class="brand-tagline">ValuTest | Remarketing | saljportalen-example.se</div>
  <div class="back-links">
    www.brolatek-example.com<br>
    www.saljportalen-example.se
  </div>
</section>

</body>
</html>
```